Nanny Share Ecommerce Website for Finding Childcare and Parents who need Childcare KindCribHelp.com

Our company needs an ecommerce website (KindCribHelp.com) for a US subscription based service strictly for nanny sharing that connects families and caregivers. The website would allow families to connect with one another as well as to search for nannies. The service would be searchable for other families by location (by radius or zip code), children demographic (age range/gender/special needs), days of week or times, after school care, school closure days (holidays), etc. The service would also be searchable for nannies based on gender, provider age range, years experience, language, hourly rate, transportation available, certification (CPR first aid), education etc. The search fields would be searchable and sortable and allow to connect with the provider (after paying subscription fee). The service would be similar to tendly.com in that it would allow for families and caregivers to post photos as well as a short bio of the themselves. There would also be a feedback/star rating mechanism to rate caregivers who have performed work for families (viewable to public). The service would be free for nannies to post their bios and only a subscription based service for families to connect with other families or with caregivers (able to view bio but need service to connect). There will be a short bio on the benefits of nanny sharing (reduced cost, increased flexibility for parents, reduced illness, increased socialization with other children vs. sole nanny), as well as Q&A section with best practices.

Target Market(s)

Families, Nannies

Industry/Entity Type

Childcare

Logo Text

Kind Crib Help

Coding

Coded - Design and coding required

Number of Pages Required

5+ page

Requirements
Must have
• Searchable (need to be able to search for families as well as nannies), responsive, functional, easy to use, add value to families and nannies. Needs to be able to collect payment for subscription.
Nice to have
• Optimized for mobile, SEO optimized

```html
<!DOCTYPE html>
<html lang="en">
<head>
<meta charset="utf-8">
<title>KindCribHelp.com – Nanny Sharing</title>
<link rel="stylesheet" href="https://fonts.googleapis.com/css2?family=Kaushan+Script&family=Raleway:wght@400;500;600;700&display=swap">
<style>
:root{
  --teal:#2fa9cc;
  --teal-dark:#1f93b6;
  --orange:#e5572c;
  --orange-soft:#e2663d;
  --ink:#2e2e2e;
  --muted:#666;
  --line:#e3e3e3;
  --footer:#27263a;
  --footer-deep:#1c1b2b;
  --footer-text:#d6d6e0;
  --white:#fff;
}
*{box-sizing:border-box;margin:0;padding:0}
html,body{width:1200px;height:3020px;overflow:hidden}
body{position:relative;background:var(--white);font-family:"Raleway",Arial,sans-serif;color:var(--ink)}
.abs{position:absolute}
.script{font-family:"Kaushan Script",cursive}

/* header */
.site-header{left:0;top:0;width:1200px;height:100px;background:var(--white)}
.brand{left:80px;top:30px;display:flex;align-items:center;gap:12px;font-weight:700;font-size:24px;color:var(--ink)}
.brand-dot{width:34px;height:34px;border-radius:50%;background:var(--orange)}
.nav-login{left:966px;top:56px;font-size:15px;color:var(--ink)}
.nav-signup{left:1026px;top:52px;width:88px;height:29px;border-radius:15px;background:var(--teal);color:var(--white);font-size:15px;text-align:center;line-height:29px}
.trim-band{left:0;top:100px;width:1200px;height:24px;background:linear-gradient(#f7e4ec,#f3d6e2)}

/* hero */
.hero{left:0;top:124px;width:1200px;height:542px;background:
  radial-gradient(ellipse at 15% 55%,#fbf1e2 0%,rgba(251,241,226,0) 55%),
  linear-gradient(180deg,#efc6dc 0%,#f4d2cf 40%,#f6c49a 75%,#f3a978 100%)}
.hero-photo{left:560px;top:124px;width:640px;height:542px;background:radial-gradient(ellipse at 45% 55%,rgba(180,60,90,.35),rgba(240,180,150,0) 65%)}
.hero-tagline{left:80px;top:248px;font-size:31px;color:var(--orange)}
.hero-title{left:80px;top:290px;font-size:46px;color:var(--teal)}
.hero-copy{left:80px;top:356px;width:480px;font-size:15px;line-height:25px;color:#333}
.hero-btn{top:459px;width:204px;height:45px;border-radius:23px;color:var(--white);display:flex;align-items:center;padding-left:34px;font-size:13px;line-height:15px}
.hero-btn b{font-family:"Kaushan Script",cursive;font-weight:400;font-size:15px;display:block;padding-left:6px}
.hero-btn svg{position:absolute;right:22px;top:15px}
.btn-parent{left:80px;background:var(--teal)}
.btn-nanny{left:300px;background:var(--orange)}

/* section titles */
.section-kicker{width:1200px;left:0;text-align:center;font-size:30px;color:var(--orange)}
.section-title{width:1200px;left:0;text-align:center;font-size:33px;font-weight:500;color:var(--ink)}

/* steps */
.step-frame{border:1px solid var(--line);background:transparent}
.step-card{border:1px solid var(--line);background:var(--white)}
.step-card h3{position:absolute;left:56px;top:34px;font-size:22px;font-weight:500}
.step{position:absolute;left:56px;width:330px}
.step svg{position:absolute;left:0;top:0}
.step h4{position:absolute;left:86px;top:0;font-size:16px;font-weight:500}
.step p{position:absolute;left:86px;top:24px;width:244px;font-size:12px;line-height:18px;color:var(--muted)}
.step-btn{position:absolute;left:60px;width:164px;height:38px;border-radius:19px;background:var(--teal);color:var(--white);text-align:center;line-height:38px;font-size:15px}
.family-art{left:912px;top:1248px;width:288px;height:212px;background:radial-gradient(ellipse at 50% 60%,#f2c9b4,rgba(255,255,255,0) 70%)}

/* caring band */
.care-band{left:0;top:1463px;width:1200px;height:577px;background:
  linear-gradient(180deg,#eef1f3 0%,#e7e6e8 45%,#d8cfd2 100%)}
.care-photo{left:640px;top:1600px;width:460px;height:440px;background:radial-gradient(ellipse at 50% 55%,rgba(210,150,120,.45),rgba(255,255,255,0) 70%)}
.care-kicker{width:1200px;left:0;top:1512px;text-align:center;font-size:30px;color:var(--orange)}
.care-title{width:1200px;left:0;top:1552px;text-align:center;font-size:47px;color:var(--teal)}
.care-sub{width:1200px;left:0;top:1622px;text-align:center;font-size:19px;font-weight:500;color:#333}
.care-btn{left:490px;top:1674px;width:218px;height:38px;border-radius:19px;background:var(--teal);color:var(--white);text-align:center;line-height:38px;font-size:15px}
.feature{width:234px;height:182px;color:var(--white);text-align:center;padding-top:52px}
.feature svg{position:absolute;left:0;top:0}
.feature h4,.feature p{position:relative}
.feature h4{font-size:16px;font-weight:500;line-height:21px;margin-bottom:6px}
.feature p{font-size:12px;line-height:16px;padding:0 28px}

/* video */
.video{left:254px;top:2212px;width:504px;height:294px;background:linear-gradient(135deg,#6f6a66,#c9b5a6 45%,#8a7f78)}
.video-face{left:400px;top:2212px;width:210px;height:294px;background:radial-gradient(ellipse at 50% 45%,rgba(240,215,195,.6),rgba(255,255,255,0) 70%)}
.vid-ctrl{left:712px;width:30px;height:30px;background:rgba(40,40,40,.75);border-radius:2px}
.vid-bar{left:272px;top:2460px;width:472px;height:32px}
.vid-name{left:700px;top:2466px;font-size:13px;font-weight:700;color:var(--white)}
.thumb{left:776px;width:162px;height:86px}

/* footer */
.footer{left:0;top:2578px;width:1200px;height:387px;background:var(--footer)}
.footer-col{top:2642px}
.footer-col h5{font-size:14px;font-weight:600;color:var(--teal);margin-bottom:10px}
.footer-col li{list-style:none;font-size:13px;line-height:21.3px;color:var(--footer-text)}
.footer-col li.more{color:var(--teal)}
.footer-base{left:0;top:2965px;width:1200px;height:55px;background:var(--footer-deep);color:#b8b8c6;font-size:11px;text-align:center;line-height:55px}
</style>
</head>
<body>

<header class="abs site-header">
  <div class="abs brand"><span class="brand-dot"></span>KindCribHelp.com</div>
  <a class="abs nav-login">Log In</a>
  <a class="abs nav-signup">Sign Up</a>
</header>
<div class="abs trim-band"></div>

<section>
  <div class="abs hero"></div>
  <div class="abs hero-photo" role="img" aria-label="Photo of a smiling mother carrying a laughing child wearing cardboard wings against a sunset sky"></div>
  <p class="abs hero-tagline script">Quality &amp; Professional Child Care</p>
  <h1 class="abs hero-title script" style="font-weight:400">At An Affordable Price</h1>
  <p class="abs hero-copy">Lorem ipsum dolor sit amet, consectetur adipiscing elit. Curabitur consequat vulputate urna. Sed vitae tortor eu nisl tempus dictum. Vivamus malesuada tristique iaculis.</p>
  <a class="abs hero-btn btn-parent"><span>Are You A Parent<b>Find Nannies</b></span>
    <svg width="16" height="14" viewBox="0 0 16 14"><path d="M1 7h13M9 2l5 5-5 5" fill="none" stroke="#fff" stroke-width="2"/></svg></a>
  <a class="abs hero-btn btn-nanny"><span>Are You A Nanny<b>Find Jobs</b></span>
    <svg width="16" height="14" viewBox="0 0 16 14"><path d="M1 7h13M9 2l5 5-5 5" fill="none" stroke="#fff" stroke-width="2"/></svg></a>
</section>

<section>
  <p class="abs section-kicker script" style="top:710px">How</p>
  <h2 class="abs section-title" style="top:744px">It Works</h2>

  <div class="abs step-frame" style="left:140px;top:829px;width:420px;height:560px"></div>
  <div class="abs step-card" style="left:124px;top:846px;width:418px;height:540px">
    <h3>Looking For Child Care?</h3>
    <div class="step" style="top:106px">
      <svg width="70" height="60" viewBox="0 0 70 60"><circle cx="35" cy="30" r="26" fill="none" stroke="#e5572c" stroke-width="3"/><circle cx="35" cy="24" r="6" fill="#2fa9cc"/><path d="M24 42c2-8 20-8 22 0" fill="none" stroke="#2fa9cc" stroke-width="3"/></svg>
      <h4>Register for free</h4>
      <p>Lorem ipsum dolor sit amet, consectetur adipiscing elit. Cras placerat maximus sodales.</p>
    </div>
    <div class="step" style="top:220px">
      <svg width="70" height="60" viewBox="0 0 70 60"><circle cx="35" cy="30" r="26" fill="none" stroke="#e5572c" stroke-width="3"/><rect x="26" y="17" width="18" height="24" fill="none" stroke="#2fa9cc" stroke-width="3"/><path d="M30 25h10M30 31h10" stroke="#2fa9cc" stroke-width="2"/></svg>
      <h4>Create your job offer</h4>
      <p>Lorem ipsum dolor sit amet, consectetur adipiscing elit. Cras placerat maximus sodales.</p>
    </div>
    <div class="step" style="top:334px">
      <svg width="70" height="60" viewBox="0 0 70 60"><circle cx="35" cy="30" r="26" fill="none" stroke="#e5572c" stroke-width="3"/><circle cx="32" cy="27" r="8" fill="none" stroke="#2fa9cc" stroke-width="3"/><path d="M38 33l7 7" stroke="#2fa9cc" stroke-width="3"/></svg>
      <h4>Search for child care</h4>
      <p>Lorem ipsum dolor sit amet, consectetur adipiscing elit. Cras placerat maximus sodales.</p>
    </div>
    <a class="step-btn script" style="top:458px">Register Now</a>
  </div>

  <div class="abs step-frame" style="left:652px;top:829px;width:420px;height:560px"></div>
  <div class="abs step-card" style="left:636px;top:846px;width:418px;height:540px">
    <h3>Looking For A Job?</h3>
    <div class="step" style="top:106px">
      <svg width="70" height="60" viewBox="0 0 70 60"><circle cx="35" cy="30" r="26" fill="none" stroke="#e5572c" stroke-width="3"/><circle cx="35" cy="24" r="6" fill="#2fa9cc"/><path d="M24 42c2-8 20-8 22 0" fill="none" stroke="#2fa9cc" stroke-width="3"/></svg>
      <h4>Register for free</h4>
      <p>Lorem ipsum dolor sit amet, consectetur adipiscing elit. Cras placerat maximus sodales.</p>
    </div>
    <div class="step" style="top:220px">
      <svg width="70" height="60" viewBox="0 0 70 60"><circle cx="35" cy="30" r="26" fill="none" stroke="#e5572c" stroke-width="3"/><rect x="26" y="17" width="18" height="24" fill="none" stroke="#2fa9cc" stroke-width="3"/><circle cx="35" cy="26" r="3" fill="#2fa9cc"/><path d="M30 35h10" stroke="#2fa9cc" stroke-width="2"/></svg>
      <h4>Create your profile</h4>
      <p>Lorem ipsum dolor sit amet, consectetur adipiscing elit. Cras placerat maximus sodales.</p>
    </div>
    <div class="step" style="top:334px">
      <svg width="70" height="60" viewBox="0 0 70 60"><circle cx="35" cy="30" r="26" fill="none" stroke="#e5572c" stroke-width="3"/><rect x="26" y="17" width="18" height="24" fill="none" stroke="#2fa9cc" stroke-width="3"/><path d="M30 29l4 4 7-8" fill="none" stroke="#2fa9cc" stroke-width="2"/></svg>
      <h4>Apply for jobs</h4>
      <p>Lorem ipsum dolor sit amet, consectetur adipiscing elit. Cras placerat maximus sodales.</p>
    </div>
    <a class="step-btn script" style="top:458px">Register Now</a>
  </div>

  <div class="abs family-art" role="img" aria-label="Illustration of a nanny with a suitcase, a mother and three children"></div>
</section>

<section>
  <div class="abs care-band" role="img" aria-label="Photo of a bright nursery with a white brick wall, toys, balloons and a mother reading to her daughter"></div>
  <div class="abs care-photo" role="img" aria-label="Mother and daughter reading a tablet together on a play mat"></div>
  <p class="abs care-kicker script">Caring Nannies</p>
  <h2 class="abs care-title script" style="font-weight:400">For Taking Care Of Your Babies</h2>
  <p class="abs care-sub">Long term, short term. Part time, full time. Anytime.</p>
  <a class="abs care-btn script">Join Our Community</a>

  <div class="abs feature" style="left:138px;top:1772px">
    <svg width="234" height="182" viewBox="0 0 234 182"><path d="M40 20C90-4 190 4 222 50c20 40-6 110-70 126C90 190 20 168 6 118-6 78 4 38 40 20z" fill="#e2663d" opacity=".92"/></svg>
    <h4>The Most Powerful<br>Nanny Search</h4>
    <p>Lorem ipsum dolor sit amet, consectetur adipiscing elit. Cras placerat.</p>
  </div>
  <div class="abs feature" style="left:478px;top:1772px">
    <svg width="234" height="182" viewBox="0 0 234 182"><path d="M40 20C90-4 190 4 222 50c20 40-6 110-70 126C90 190 20 168 6 118-6 78 4 38 40 20z" fill="#e2663d" opacity=".92"/></svg>
    <h4>Proven &amp; Trustworthy<br>Nannies</h4>
    <p>Lorem ipsum dolor sit amet, consectetur adipiscing elit. Cras placerat.</p>
  </div>
  <div class="abs feature" style="left:824px;top:1772px">
    <svg width="234" height="182" viewBox="0 0 234 182"><path d="M40 20C90-4 190 4 222 50c20 40-6 110-70 126C90 190 20 168 6 118-6 78 4 38 40 20z" fill="#e2663d" opacity=".92"/></svg>
    <h4>Easily Book<br>Interviews &amp; Jobs</h4>
    <p>Lorem ipsum dolor sit amet, consectetur adipiscing elit. Cras placerat.</p>
  </div>
</section>

<section>
  <p class="abs section-kicker script" style="top:2088px">Why</p>
  <h2 class="abs section-title" style="top:2122px">We hire nannies</h2>

  <div class="abs video" role="img" aria-label="Video still of a nanny speaking to camera"></div>
  <div class="abs video-face" role="img" aria-label="Nanny portrait in video"></div>
  <div class="abs vid-ctrl" style="top:2236px"><svg width="30" height="30" viewBox="0 0 30 30"><path d="M15 21l-6-6a3.5 3.5 0 0 1 6-4 3.5 3.5 0 0 1 6 4z" fill="#fff"/></svg></div>
  <div class="abs vid-ctrl" style="top:2270px"><svg width="30" height="30" viewBox="0 0 30 30"><circle cx="15" cy="15" r="6" fill="none" stroke="#fff" stroke-width="2"/><path d="M15 11v4h3" stroke="#fff" stroke-width="1.5" fill="none"/></svg></div>
  <div class="abs vid-ctrl" style="top:2304px"><svg width="30" height="30" viewBox="0 0 30 30"><path d="M8 15l14-6-6 14-2-6z" fill="#fff"/></svg></div>
  <svg class="abs vid-bar" viewBox="0 0 472 32" width="472" height="32">
    <rect x="0" y="0" width="42" height="32" rx="2" fill="rgba(30,30,30,.85)"/>
    <path d="M16 9l12 7-12 7z" fill="#fff"/>
    <rect x="46" y="0" width="426" height="32" rx="2" fill="rgba(30,30,30,.75)"/>
    <rect x="54" y="12" width="290" height="8" fill="#555"/>
    <rect x="54" y="12" width="24" height="8" fill="#999"/>
    <rect x="54" y="0" width="30" height="10" fill="#fff"/>
    <circle cx="374" cy="16" r="4" fill="none" stroke="#fff" stroke-width="2"/>
  </svg>
  <span class="abs" style="left:328px;top:2461px;font-size:8px;color:#333">02:06</span>
  <span class="abs vid-name">Clipway</span>

  <div class="abs thumb" style="top:2212px;background:linear-gradient(135deg,#3a6b63,#c9a795)" role="img" aria-label="Portrait thumbnail of a nanny"></div>
  <div class="abs thumb" style="top:2315px;background:linear-gradient(135deg,#e8e4e0,#9b6b55)" role="img" aria-label="Portrait thumbnail of a nanny"></div>
  <div class="abs thumb" style="top:2420px;background:linear-gradient(135deg,#f2efe8,#d9a977)" role="img" aria-label="Portrait thumbnail of a nanny"></div>
</section>

<footer>
  <div class="abs footer"></div>
  <div class="abs footer-col" style="left:80px"><h5>Discover</h5><ul>
    <li>Parents: How it Works</li><li>Sitters: How it Works</li><li>Gift Cards</li><li>Childcare Resources</li><li>Get the App</li><li>Find Schools and Groups</li><li>Pricing</li><li>Support</li></ul></div>
  <div class="abs footer-col" style="left:292px"><h5>Company</h5><ul>
    <li>About Us</li><li>Press</li><li>Corporate Benefits</li><li>Careers at SitterNest</li><li>Affiliate Program</li><li>Babysitting Jobs</li><li>Nanny Jobs</li><li>Terms of Service</li><li>Privacy Policy</li></ul></div>
  <div class="abs footer-col" style="left:482px"><h5>Nannies near me</h5><ul>
    <li>San Francisco Nannies</li><li>New York City Nannies</li><li>Chicago Nannies</li><li>Los Angeles Nannies</li><li>Seattle Nannies</li><li>Portland Nannies</li><li>Washington DC Nannies</li><li>Boston Nannies</li><li>Denver Nannies</li><li>San Diego Nannies</li><li class="more">See all cities »</li></ul></div>
  <div class="abs footer-col" style="left:692px"><h5>Programs/Resources</h5><ul>
    <li>Community</li><li>Child Care Articles &amp; Resources</li><li>Pet Care Articles &amp; Resources</li><li>Senior Care Articles &amp; Resources</li><li>House &amp; Home Articles and Resources</li><li>Ask a Question</li><li>Post a Story</li><li>Explore Topics</li><li>How-to Guides</li><li>Research &amp; Data</li></ul></div>
  <div class="abs footer-col" style="left:972px"><h5>Follow KindCribHelp</h5><ul>
    <li>Kinnect</li><li>Pictly</li><li>Chirper</li><li>Orbit+</li><li>Childcare Blog</li><li>Pinboardly</li><li>ClipStream</li></ul></div>
  <div class="abs footer-base">Copyrights 2018 KindCribHelp.com. All Rights Reserved.</div>
</footer>

</body>
</html>
```